Baseline Court Partners needs a business card

I need a business card design for a new company
For the last 10 years I have ran a tennis management company called Silver Ridge Racquet (www.silverridgeracquet.example)
The new company - Baseline Court Partners (BCP) will replace SRRA starting this winter
The goal of BCP will be to expand our operations into new clubs as well and a revenue stream from existing clubs with courtdeskhub.example
We plan to go regional in 2014 and then look outward from there

Target Market(s)

small to medium sized tennis facilities both public and private
Our market are the clubs - not the players
This includes private clubs, municipalities, recreation assc, etc

Industry/Entity Type

Business

Requirements
Must have
• Glen Harwick
• President
• 555-204-1839 Office
• 555-317-9052 Cell
• gharwick@baselinecourtpartners.example
• www.baselinecourtpartnres.example
Nice to have
• One of the unique benefits to a company joining BCP will be integration into our web based club software service - Courtdeskhub.example
• We have developed this turnkey service for small to medium sized clubs and re the exclusive providers of it
Should not have
• address or state

```html
<!DOCTYPE html>
<html lang="en">
<head>
<meta charset="utf-8">
<title>Baseline Court Partners – Business Card</title>
<link rel="stylesheet" href="https://fonts.googleapis.com/css2?family=Questrial&display=swap">
<style>
  :root {
    --backdrop: #e9e6e1;
    --court-deep: #1f4a2c;
    --court-mid: #2d6a3b;
    --court-light: #3f7d47;
    --line-white: #f3f4f1;
    --brand-yellow: #f2c81a;
    --text-light: #e6e9e4;
    --text-soft: #c9d2c9;
  }
  * { margin: 0; padding: 0; box-sizing: border-box; }
  html, body {
    width: 1200px;
    height: 1000px;
    overflow: hidden;
    background: var(--backdrop);
  }
  .canvas {
    position: relative;
    width: 1200px;
    height: 1000px;
  }
  .business-card {
    position: absolute;
    left: 180px;
    top: 260px;
    width: 840px;
    height: 480px;
    overflow: hidden;
    border-radius: 4px;
    box-shadow: 0 14px 34px rgba(0, 0, 0, 0.22);
    font-family: "Questrial", sans-serif;
  }
  .court-photo {
    position: absolute;
    inset: 0;
    background:
      radial-gradient(circle at 24% 34%, rgba(214, 230, 60, 0.55) 0 70px, transparent 72px),
      linear-gradient(176deg, transparent 0 39%, rgba(243, 244, 241, 0.85) 40% 46%, transparent 47%),
      linear-gradient(180deg, #16321f 0%, var(--court-light) 18%, var(--court-mid) 45%, var(--court-deep) 100%);
  }
  .brand-block {
    position: absolute;
    right: 60px;
    bottom: 92px;
    display: flex;
    align-items: center;
    gap: 12px;
  }
  .brand-name {
    font-size: 40px;
    color: var(--text-light);
    letter-spacing: 0.5px;
  }
  .brand-dot {
    width: 22px;
    height: 22px;
    border-radius: 50%;
    background: var(--brand-yellow);
  }
  .web-address {
    position: absolute;
    right: 60px;
    bottom: 52px;
    font-size: 17px;
    letter-spacing: 2px;
    color: var(--text-soft);
  }
</style>
</head>
<body>
  <main class="canvas">
    <section class="business-card">
      <div class="court-photo" role="img" aria-label="Photo of a yellow tennis ball resting on the white line of a green court, with the net blurred behind"></div>
      <div class="brand-block">
        <span class="brand-name">courtdeskhub</span>
        <span class="brand-dot"></span>
      </div>
      <p class="web-address">www.baselinecourtpartnres.example</p>
    </section>
  </main>
</body>
</html>
```